Specialised investor in e-mobility and energy wants business card design

We need a business card design that fits our existing corporate design. <The look and feel must be 'sharp'/'clean', dynamic, communicate momentum, professionalism etc (as one would imagine from a firm in the financial sector). We like the idea of a reverse-side of the card that includes the logo, and the name and contact details on the other. We expect the deliverable to be whatever format might be required to be able to get cards printed directly by a service such as tandor press. Our website is www.orm.capital

```html
<!DOCTYPE html>
<html lang="en">
<head>
<meta charset="utf-8">
<title>ORM Capital – Business Card</title>
<link href="https://fonts.googleapis.com/css2?family=Arimo:wght@400;700&display=swap" rel="stylesheet">
<style>
  :root {
    --bg: #e3e4e6;
    --green-dark: #2f4f23;
    --green-mid: #3f6b2a;
    --green-light: #86b54a;
    --green-bright: #9ccb55;
    --white: #ffffff;
  }
  * { margin: 0; padding: 0; box-sizing: border-box; }
  html, body { width: 1200px; height: 800px; overflow: hidden; }
  body {
    background: var(--bg);
    font-family: "Arimo", Arial, sans-serif;
    position: relative;
  }
  .card {
    position: absolute;
    width: 520px;
    height: 336px;
    top: 232px;
    overflow: hidden;
    box-shadow: 0 6px 18px rgba(0,0,0,0.12);
  }
  .card--front { left: 50px; }
  .card--back { left: 630px; }
  .card__shapes { position: absolute; inset: 0; width: 100%; height: 100%; }

  .brand-name {
    position: absolute;
    font-weight: 400;
    color: var(--green-dark);
    white-space: nowrap;
    line-height: 1;
  }
  .card--front .brand-name { left: 44px; top: 250px; font-size: 40px; }
  .card--back .brand-name { right: 16px; top: 268px; font-size: 25px; }

  .web-url {
    position: absolute;
    right: 26px;
    top: 110px;
    font-size: 15px;
    letter-spacing: 5px;
    color: var(--green-bright);
  }
  .web-url span { color: var(--white); }

  .holder { position: absolute; left: 30px; top: 24px; color: var(--white); }
  .holder__role { font-size: 12px; }
  .holder__name { font-size: 15px; font-weight: 700; color: var(--green-bright); letter-spacing: 0.3px; margin-top: 2px; }
  .holder__phone { font-size: 12px; margin-top: 6px; display: flex; align-items: center; gap: 8px; }

  .contact-list { position: absolute; left: 30px; top: 140px; list-style: none; color: var(--white); font-size: 12.5px; }
  .contact-list li { display: flex; align-items: center; gap: 8px; margin-bottom: 7px; }
  .contact-list strong { font-weight: 700; }
  .icon { width: 12px; height: 12px; flex: none; }
</style>
</head>
<body>

<section class="card card--front" aria-label="Card front">
  <svg class="card__shapes" viewBox="0 0 520 336" aria-hidden="true">
    <defs>
      <linearGradient id="frontLight" x1="0" y1="0" x2="1" y2="0">
        <stop offset="0" stop-color="#6fa634"/>
        <stop offset="1" stop-color="#97c852"/>
      </linearGradient>
    </defs>
    <rect width="520" height="336" fill="url(#frontLight)"/>
    <polygon points="0,0 190,0 330,180 0,205" fill="var(--white)"/>
    <polygon points="0,205 330,180 338,190 0,218" fill="var(--green-mid)"/>
    <polygon points="190,0 520,0 520,336 500,336 330,180" fill="var(--green-dark)"/>
    <polygon points="190,0 200,0 338,190 330,180" fill="var(--green-light)"/>
  </svg>
  <p class="web-url"><span>www.</span>orm.capital</p>
  <p class="brand-name">ORM Capital</p>
</section>

<section class="card card--back" aria-label="Card back">
  <svg class="card__shapes" viewBox="0 0 520 336" aria-hidden="true">
    <rect width="520" height="336" fill="var(--green-dark)"/>
    <polygon points="0,110 290,110 345,336 0,336" fill="var(--green-light)"/>
    <polygon points="290,110 300,110 357,336 345,336" fill="var(--green-mid)"/>
    <polygon points="305,110 520,170 520,336 360,336" fill="var(--white)"/>
  </svg>

  <div class="holder">
    <p class="holder__role">Partner</p>
    <p class="holder__name">ELIAS MARNOCH</p>
    <p class="holder__phone">
      <svg class="icon" viewBox="0 0 12 12" aria-hidden="true"><rect x="3" y="0.5" width="6" height="11" rx="1" fill="none" stroke="#9ccb55"/><circle cx="6" cy="9.5" r="0.7" fill="#9ccb55"/></svg>
      +41 79555 0148
    </p>
  </div>

  <ul class="contact-list">
    <li>
      <svg class="icon" viewBox="0 0 12 12" aria-hidden="true"><rect x="0.5" y="2.5" width="11" height="7" fill="#fff"/><path d="M0.5 2.5 L6 7 L11.5 2.5" fill="none" stroke="#86b54a"/></svg>
      elias@orm.capital
    </li>
    <li>
      <svg class="icon" viewBox="0 0 12 12" aria-hidden="true"><circle cx="6" cy="6" r="5" fill="none" stroke="#fff"/><ellipse cx="6" cy="6" rx="2" ry="5" fill="none" stroke="#fff"/><line x1="1" y1="6" x2="11" y2="6" stroke="#fff"/></svg>
      www.orm.capital
    </li>
    <li>
      <svg class="icon" viewBox="0 0 12 12" aria-hidden="true"><path d="M6 11.5 C3 7.5 2 6 2 4.3 A4 4 0 0 1 10 4.3 C10 6 9 7.5 6 11.5Z" fill="#fff"/><circle cx="6" cy="4.3" r="1.4" fill="#86b54a"/></svg>
      <span><strong>ORM Capital S.A.</strong> Geneva, Switzerland</span>
    </li>
  </ul>

  <p class="brand-name">ORM Capital</p>
</section>

</body>
</html>
```